Postcard for harbor crest homes

Create new 6.5 x 9 postcard for harbor crest homes.
FRONT: See attached postcard for the front, change Keystone Nest logo with Harbor Crest Homes logo. change Keystone Nest above the phone # to Harbor Crest Homes Myrtle Beach.
BACK: See attachment for text on the back. add postage and pictures to make it look professional.

```html
<!DOCTYPE html>
<html lang="en">
<head>
<meta charset="utf-8">
<title>Harbor Crest Homes – Postcard</title>
<link rel="stylesheet" href="https://fonts.googleapis.com/css2?family=Open+Sans:ital,wght@0,400;0,600;0,700;0,800;1,700&family=Roboto+Condensed:wght@400;700&display=swap">
<style>
  :root{
    --teal:#1f5d75;
    --teal-light:#2b7c96;
    --teal-dark:#164559;
    --yellow:#f6b437;
    --yellow-deep:#e59a22;
    --white:#ffffff;
    --paper:#f3f4f5;
    --stage:#e6e8ea;
    --ink:#1b3d4d;
    --photo-warm:#cdb39a;
    --photo-light:#eee4d8;
  }
  *{box-sizing:border-box;margin:0;padding:0}
  html,body{width:902px;height:1200px;overflow:hidden}
  body{background:var(--stage);font-family:"Open Sans",sans-serif;position:relative}
  .card{position:absolute;left:71px;width:760px;height:549px;background:var(--white);overflow:hidden;box-shadow:0 6px 18px rgba(0,0,0,.18)}
  .card--front{top:34px}
  .card--back{top:617px}
  .card svg.shapes{position:absolute;inset:0;width:100%;height:100%}
  .abs{position:absolute}
  .cond{font-family:"Roboto Condensed",sans-serif}

  /* brand mark */
  .brand{display:flex;align-items:center;gap:8px;color:var(--teal);font-weight:700;white-space:nowrap}
  .brand__dot{width:16px;height:16px;border-radius:50%;background:var(--yellow);flex:none}

  /* front */
  .front-brand{left:30px;top:84px;font-size:24px}
  .front-photo{left:285px;top:0;width:475px;height:318px;
    background:linear-gradient(135deg,var(--photo-light),var(--photo-warm) 60%,#8c7463);
    clip-path:polygon(0 0,100% 0,100% 94%,30% 100%,0 24%)}
  .sell-house{left:40px;top:246px;width:200px;height:112px}
  .sell{left:66px;top:268px;font-size:56px;font-weight:800;color:var(--white);line-height:1;letter-spacing:-1px}
  .your-home{left:64px;top:328px;width:166px;height:30px;background:var(--yellow);color:var(--teal-dark);
    font-size:21px;font-weight:800;text-align:center;line-height:30px}
  .as-low{left:62px;top:362px;font-size:24px;color:var(--white);font-weight:400;line-height:1.2}
  .percent{left:262px;top:250px;font-size:120px;font-weight:700;color:var(--white);line-height:1;letter-spacing:-3px}
  .commission{left:60px;top:392px;font-size:48px;font-weight:800;color:var(--yellow);letter-spacing:-1px;line-height:1.1}
  .front-points{left:465px;top:338px;width:275px;list-style:none;color:var(--white);font-size:14px;font-weight:600;line-height:1.35}
  .front-points li{position:relative;padding-left:22px;margin-bottom:16px}
  .front-points li::before{content:"";position:absolute;left:0;top:5px;width:9px;height:9px;border-radius:50%;background:var(--yellow)}
  .front-phone{left:70px;top:458px;display:flex;align-items:center;gap:12px}
  .phone-icon{width:34px;height:34px;border-radius:50%;background:var(--teal-dark);display:flex;align-items:center;justify-content:center;flex:none}
  .front-phone__num{font-size:40px;font-weight:700;color:var(--teal-dark);letter-spacing:-.5px;line-height:1}
  .front-tagline{left:110px;top:510px;font-size:19px;color:var(--yellow);white-space:nowrap}

  /* back */
  .ribbon-save{left:58px;top:78px;height:62px;background:var(--yellow);padding:0 14px;display:flex;align-items:center;gap:10px}
  .ribbon-save__big{font-size:46px;font-weight:700;color:var(--teal-dark);line-height:1}
  .ribbon-save__stack{display:flex;flex-direction:column;line-height:1}
  .ribbon-save__thousands{font-size:30px;font-weight:700;color:var(--teal-dark)}
  .ribbon-save__fees{font-size:15px;font-weight:700;color:var(--white);background:var(--teal-dark);padding:2px 6px;margin-top:2px}
  .back-note{left:120px;top:148px;font-size:11px;color:var(--white)}
  .back-head{left:38px;top:166px;font-size:30px;font-weight:700;color:var(--white);letter-spacing:-.3px}
  .back-points{left:40px;top:208px;list-style:none;color:var(--white);font-size:10.5px;font-weight:700;font-style:italic;line-height:1.6}
  .back-points li{position:relative;padding-left:14px}
  .back-points li::before{content:"";position:absolute;left:0;top:6px;width:6px;height:6px;border-radius:50%;background:var(--yellow)}
  .back-photo{left:356px;top:322px;width:108px;height:146px;border-radius:54px 54px 0 0;
    background:linear-gradient(180deg,#b98a6b,#e9e6ee 55%,#d7d3dd)}
  .worth-head{left:50px;top:318px;font-size:22px;font-weight:700;color:var(--white)}
  .worth-box{left:50px;top:352px;width:296px;height:104px;background:var(--yellow);padding:10px 16px;
    color:var(--teal-dark);font-size:11.5px;font-weight:700;line-height:1.4}
  .worth-box__mail{display:block;margin-top:4px;font-size:13px}
  .agents{left:70px;top:470px;display:flex;gap:14px}
  .agent{width:72px;text-align:center}
  .agent__photo{width:72px;height:46px;background:linear-gradient(180deg,#c9cdd2,#8d949b)}
  .agent__name{background:var(--teal-dark);color:var(--white);font-size:10px;font-weight:700;line-height:1.2;padding:2px 0}
  .agent__role{display:block;font-size:8px;font-weight:600}
  .back-phone{left:242px;top:470px;width:222px;height:34px;background:var(--teal-dark);display:flex;align-items:center;gap:10px;padding-left:8px}
  .back-phone .phone-icon{width:26px;height:26px;background:var(--white)}
  .back-phone__num{font-size:27px;font-weight:700;color:var(--white);line-height:1}
  .back-address{left:262px;top:510px;display:flex;gap:6px;color:var(--teal-dark);font-size:11px;font-weight:700;line-height:1.3}
  .back-brand{left:490px;top:48px;font-size:14px}
  .postage{left:662px;top:22px;width:84px;height:66px;border:1px solid #777;font-size:8.5px;line-height:1.3;color:#333;text-align:center;padding-top:5px;white-space:nowrap}
  .address-box{left:500px;top:250px;width:218px;height:72px;border:1px solid #888;font-size:11px;color:#333;padding:26px 0 0 14px;line-height:1.3}
</style>
</head>
<body>

<!-- FRONT -->
<section class="card card--front" aria-label="Postcard front">
  <svg class="shapes" viewBox="0 0 760 549" aria-hidden="true">
    <defs>
      <linearGradient id="tealFront" x1="0" y1="0" x2="1" y2="1">
        <stop offset="0" stop-color="#2b7c96"/><stop offset="1" stop-color="#174a5f"/>
      </linearGradient>
    </defs>
    <polygon points="0,238 305,238 445,322 760,302 760,490 470,528 452,549 0,549" fill="url(#tealFront)"/>
    <polygon points="0,452 462,446 448,549 0,549" fill="#f3f4f5"/>
    <polygon points="470,528 760,490 760,549 452,549" fill="#eef0f1"/>
    <polygon points="60,504 455,498 449,538 44,546" fill="#164559"/>
  </svg>

  <div class="abs brand front-brand"><span class="brand__dot"></span>Harbor Crest Homes</div>

  <div class="abs front-photo" role="img" aria-label="Photo of a smiling couple on a sofa shaking hands with a real estate agent"></div>

  <svg class="abs sell-house" viewBox="0 0 200 112" aria-hidden="true">
    <polyline points="16,110 16,48 96,6 176,48 176,66" fill="none" stroke="#f6b437" stroke-width="7" stroke-linejoin="miter"/>
    <rect x="134" y="14" width="14" height="24" fill="#f6b437"/>
  </svg>
  <div class="abs sell">SELL</div>
  <div class="abs your-home">YOUR HOME</div>
  <div class="abs as-low">FOR AS LOW AS</div>
  <div class="abs percent cond">2%</div>
  <div class="abs commission">COMMISSION</div>

  <ul class="abs front-points">
    <li>We list for 2%. If a buyer contacts us about your property, we handle the whole transaction for 2%.</li>
    <li>The Buyer's agent commission is 2%. If an agent from another company sells your property, the total commission is 4%.</li>
  </ul>

  <div class="abs front-phone">
    <span class="phone-icon">
      <svg width="18" height="18" viewBox="0 0 24 24" aria-hidden="true"><path fill="#f6b437" d="M6.6 10.8a15.1 15.1 0 0 0 6.6 6.6l2.2-2.2c.3-.3.7-.4 1-.2 1.1.4 2.3.6 3.6.6.6 0 1 .4 1 1V20c0 .6-.4 1-1 1A17 17 0 0 1 3 4c0-.6.4-1 1-1h3.5c.6 0 1 .4 1 1 0 1.3.2 2.5.6 3.6.1.3 0 .7-.2 1z"/></svg>
    </span>
    <span class="front-phone__num cond">843-555-0142</span>
  </div>
  <div class="abs front-tagline">Harbor Crest Homes Myrtle Beach</div>
</section>

<!-- BACK -->
<section class="card card--back" aria-label="Postcard back">
  <svg class="shapes" viewBox="0 0 760 549" aria-hidden="true">
    <defs>
      <linearGradient id="tealBack" x1="0" y1="0" x2="1" y2="1">
        <stop offset="0" stop-color="#174a5f"/><stop offset="1" stop-color="#2b7c96"/>
      </linearGradient>
    </defs>
    <polygon points="0,62 470,28 470,470 0,470" fill="url(#tealBack)"/>
    <polygon points="0,470 470,470 470,549 0,549" fill="#f3f4f5"/>
    <polygon points="28,128 58,104 58,140" fill="#e59a22"/>
  </svg>

  <div class="abs ribbon-save cond">
    <span class="ribbon-save__big">SAVE</span>
    <span class="ribbon-save__stack">
      <span class="ribbon-save__thousands">THOUSANDS</span>
      <span class="ribbon-save__fees">IN COMMISSION FEES.</span>
    </span>
  </div>

  <div class="abs back-note">We have local knowledge with over 1,000 closings in Horry County</div>
  <div class="abs back-head cond">WE ARE NOT A DISCOUNT BROKER.</div>
  <ul class="abs back-points">
    <li>We meet with you for in-home consultation</li>
    <li>We list in the MLS</li>
    <li>Professional photography, lockbox, and yard sign.</li>
    <li>Internet marketing, HomeScout, ListPoint and 80 websites.</li>
    <li>Handle all paperwork, offers and negotiations.</li>
    <li>Manage inspections and closing.</li>
  </ul>

  <div class="abs back-photo" role="img" aria-label="Photo of a smiling woman pointing toward the offer text"></div>

  <div class="abs worth-head cond">WHAT'S YOUR HOME WORTH?</div>
  <div class="abs worth-box">
    Receive a no obligation email.<br>
    We research comparable sales to find the best price for your home.<br>
    Send us an email with the property address.
    <span class="worth-box__mail">hello@HarborCrestHomesMB.com</span>
  </div>

  <div class="abs agents">
    <div class="agent">
      <div class="agent__photo" role="img" aria-label="Headshot of broker Dale Corwin"></div>
      <div class="agent__name">Dale Corwin<span class="agent__role">Broker</span></div>
    </div>
    <div class="agent">
      <div class="agent__photo" role="img" aria-label="Headshot of realtor Nora Pell"></div>
      <div class="agent__name">Nora Pell<span class="agent__role">Realtor</span></div>
    </div>
  </div>

  <div class="abs back-phone">
    <span class="phone-icon">
      <svg width="14" height="14" viewBox="0 0 24 24" aria-hidden="true"><path fill="#164559" d="M6.6 10.8a15.1 15.1 0 0 0 6.6 6.6l2.2-2.2c.3-.3.7-.4 1-.2 1.1.4 2.3.6 3.6.6.6 0 1 .4 1 1V20c0 .6-.4 1-1 1A17 17 0 0 1 3 4c0-.6.4-1 1-1h3.5c.6 0 1 .4 1 1 0 1.3.2 2.5.6 3.6.1.3 0 .7-.2 1z"/></svg>
    </span>
    <span class="back-phone__num cond">843-555-0142</span>
  </div>
  <div class="abs back-address">
    <svg width="10" height="14" viewBox="0 0 10 14" aria-hidden="true"><path fill="#164559" d="M5 0a5 5 0 0 0-5 5c0 3.6 5 9 5 9s5-5.4 5-9a5 5 0 0 0-5-5zm0 7a2 2 0 1 1 0-4 2 2 0 0 1 0 4z"/></svg>
    <span>410 Tidewater Ln<br>Myrtle Beach, SC 29577</span>
  </div>

  <div class="abs brand back-brand"><span class="brand__dot"></span>Harbor Crest Homes</div>

  <div class="abs postage">PRSRT STD<br>ECRWSS<br>U.S.POSTAGE<br>PAID<br>EDDM Retail</div>
  <div class="abs address-box">Local<br>Postal Customer</div>
</section>

</body>
</html>
```